Creating business cards for our new private medical clinic in London

Hey everyone,

We are starting a new private medical clinic in central London. We already have our logo (please see the 2 different layouts of the logo attached.) Please note that we are not restricted to using only this font in the card though.

The cards will be printed by "Pekko." The cards have a textured surface and a coloured middle layer - please see this webpage for the exact product spec (https://www.pekkoprint.example/uk/products/velvet/business-cards.html). We're overall looking for a modern yet highly professional look. We'd like the cards to have Square edges and NOT rounded please.

We need a standard card that uses one or both of our logo's colours (blue and green), and another card for premium customers, that uses black with either gold/silver/bronze. On the black coloured cads, please could you add the word "Black Account" or the word "Black" under the logo text - wherever you think it looks best?

_________________

AMENDMENT TO BRIEF:

1) The first batch of our cards are to be promotional cards and need to have more information. Could please have one card that is more like an "information card" that has the following information: - (There's a lot there and we might need to slim this down once we see the cards.)

GP appointments £70
-Feeling unwell
-Referrals to private specialists
-Sexual health check up
-Contraception
-Second opinion

Launch Offer
First appointment £40 with this card until 30 September 2017

Book online

2) Could you see whether we could add a 'strap line' to the card, something like: “Stay in Optimal Health”

_____________

The files attached have 2 versions of our logo - one linear and with the words 'stacked'; we think that the stacked logo may work better for the business card but we'd love to see different versions.

On one side of the card could we please see a coloured background, with a design containing our logo? On the other side of the card, please could we have a different coloured or white background and the information below.

Address: THE HARROWFIELD CLINIC @ FitVanta, 19 Bramblecote Lane, London, EC2Z 4QJ
Open: Mon-Fri (early & late appointments)
Book Online: www.harrowfieldclinic.example
Email: bookings@harrowfieldclinic.example
Phone number: (We don't have this yet - but please leave a space for this to go into.)

Other possible design features:

Because our clinic is located in the financial district of London, anything that represents this (e.g. The City of London's skyline - i.e. financial district - could look nice (example buildings include: The Pinecone, The Teacup-Tower, The Wedgehouse, St Aldric Minster, Keep of Brennmoor, Gantry Crossing, The Spindle). We wondered whether a outline or drawing of these buildings in the background of the card could look nice. Please see the image link below to get an idea of the skyline we're looking for:

https://img.stockvale.example/z/skyline-hand-drawn-city-pastel-shades-heritage-buildings-futuristic-81920457.jpg

The following image links are examples of cards that we've seen online and like the overall feel of (of course our colours are different):

http://www.craftnook.example/diverse/2/goodcards/73014589122.jpg
http://cardheron.example/wp-content/uploads/2013/01/cool-business-cards-saffron.jpg
https://cardfolio.example/wp-content/uploads/20461-cool-business-card-mockup.jpg
http://www.plinthworks.example/wp-content/uploads/edd/2015/08/Modern-Tutor-Business-Card-Template-Preview.jpg
http://lorvelandkit.example/wp-content/uploads/2017/01/design-a-business-card-cool-business-card-designsqx83.jpg
http://makerspindle.example/resources/files/articles/harbor-print/copper-foil-business-cards.jpg

STATIONARY:
We will also need the following stationary designed by our chosen designer. We’d like stationary to use one or both the colours of our logo (ie Green and Blue). Please use these colours to add any additional design features to stationary - other similar palette colours can also be used. Our logo font is - abeatbyKai - and this could be used in other parts of the stationary, but please feel free to try other fonts too. We prefer sans serif fonts.

Overall - we are open to all ideas but we need a look and feel that looks modern and highly professional. For our letter, prescription and medical report templates we need these to be PDFs and word processing files that can merge relevant data and text into different sections.

The information required on various pieces of stationary are as follows:

Letterheads:
These need to have:
Clinic's: Logo / Address / Phone Number / Website / Email address / Recipients address.
The letter can have address data either at the top or as a footer. We're happy to see designs that use either to see which one looks best (same goes for other pieces of stationary too.)

Invoices:
Invoice number: (Unique code for document)
Invoice Date:
Clinic’s: Logo / Address / Phone Number / Website / Email address
Services: Service Code / Name of Service / Price
Total Price:
PAYLO, Cardwise and Northern Remit Logos
Patient details: Patient’s Name / Address

Prescription Pads:
Prescription number: (Unique code for document)
Clinic details: Clinic’s Logo / Address / Phone Number / Website / Email address
Patient details needed include: Patient’s Name / Date of birth / address
Blank space required to write the name of medication
Doctors Signature: and space for signature
MPB Number: and space for this to be entered

Templates for our medical reports:
These are reports we will be printed (on good quality paper) for patients after they have had a complete health check. They will include a text summary, and the results of any tests (with graphs) and images of scans. Please could we see how text/titles/headings/tables etc could be styled?
They will need the following details: -
Clinic details needed include: Clinic’s Logo / Address / Phone Number / Website / Email address
Date of Report:
Then the following sections need to be includes:
1) Free Text Space
2) Space for images and text
3) Space for blood test and text

___________________

Thanks so much everyone.

All the best,

Tev and Dane

Target Market(s)

City of London
Private Healthcare

Industry/Entity Type

Health Care

Contact Information for Business Card

Font styles to use
Sans Serif

Colors
33a6d7
25a0d3
add136
9bcb3c
cadf82
85acd3
3276b5
0255a3
85cae6

Requirements
Must have
• Please see project description for details.
Nice to have
• Perhaps a outline/drawing/illustration of the City of London skyline (i.e. the Pinecone and surrounding buildings)

```html
<!DOCTYPE html>
<html lang="en">
<head>
<meta charset="utf-8">
<title>The Harrowfield Clinic – Letterhead</title>
<link rel="stylesheet" href="https://fonts.googleapis.com/css2?family=Comfortaa:wght@400&family=Open+Sans:wght@400;600&display=swap">
<style>
  :root {
    --clinic-blue: #55b7de;
    --clinic-green: #add136;
    --ink: #3a3a3a;
    --muted: #7a7a7a;
    --skyline-grey: #e3e3e3;
    --backdrop: #e9e9ea;
    --paper: #ffffff;
  }
  * { margin: 0; padding: 0; box-sizing: border-box; }
  html, body {
    width: 1200px; height: 886px; overflow: hidden;
    background: var(--backdrop);
    font-family: "Open Sans", sans-serif;
  }
  .letterhead {
    position: absolute;
    left: 300px; top: 19px;
    width: 600px; height: 848px;
    background: var(--paper);
    box-shadow: 0 2px 10px rgba(0,0,0,0.12);
    overflow: hidden;
  }
  .corner-blue {
    position: absolute; top: 0; right: 52px;
    width: 40px; height: 16px;
    background: var(--clinic-blue);
  }
  .corner-green {
    position: absolute; top: 0; right: 0;
    width: 52px; height: 40px;
    background: var(--clinic-green);
  }
  .brand {
    position: absolute; left: 44px; top: 92px;
    display: flex; align-items: center; gap: 12px;
  }
  .brand-square {
    width: 34px; height: 34px;
    background: var(--clinic-blue);
  }
  .brand-divider {
    width: 1px; height: 58px; background: var(--clinic-blue);
  }
  .brand-name {
    font-family: "Comfortaa", sans-serif;
    font-weight: 400;
    color: var(--clinic-blue);
    font-size: 22px; line-height: 1.05;
  }
  .brand-tagline {
    font-size: 7px; letter-spacing: 0.12em;
    color: var(--muted); margin-top: 5px;
  }
  .contact {
    position: absolute; right: 70px; top: 62px;
    list-style: none;
    font-size: 8px; line-height: 1.35; color: var(--ink);
    font-weight: 600;
  }
  .contact li { display: flex; gap: 7px; margin-bottom: 5px; }
  .contact svg { flex: none; margin-top: 1px; }
  .skyline {
    position: absolute; right: 0; bottom: 40px;
    width: 380px; height: 330px;
    background: linear-gradient(to top, var(--skyline-grey), rgba(227,227,227,0.35));
    clip-path: polygon(0 100%, 0 75%, 20% 62%, 35% 40%, 52% 28%, 68% 14%, 85% 0, 100% 6%, 100% 100%);
  }
  .footer-bands {
    position: absolute; left: 0; bottom: 0;
    width: 600px; height: 40px;
  }
</style>
</head>
<body>
  <main class="letterhead">
    <div class="corner-blue"></div>
    <div class="corner-green"></div>

    <header class="brand">
      <div class="brand-square"></div>
      <div class="brand-divider"></div>
      <div>
        <div class="brand-name">The Harrowfield<br>Clinic</div>
        <div class="brand-tagline">PRIVATE GENERAL PRACTICE</div>
      </div>
    </header>

    <ul class="contact">
      <li>
        <svg width="7" height="9" viewBox="0 0 10 13"><path d="M5 0a5 5 0 0 0-5 5c0 4 5 8 5 8s5-4 5-8a5 5 0 0 0-5-5z" fill="#add136"/><circle cx="5" cy="5" r="2" fill="#fff"/></svg>
        <span>Harrowfield Clinic @FitVanta,<br>19 Bramblecote Lane<br>London, EC2Z 4QJ</span>
      </li>
      <li>
        <svg width="8" height="8" viewBox="0 0 10 10"><path d="M2 0l2 2.5-1 1.2c.6 1.3 1.6 2.3 2.9 2.9L7 5.5 10 7.5 9 10C4 9.5.5 6 0 1z" fill="#add136"/></svg>
        <span>00 0000 0000</span>
      </li>
      <li>
        <svg width="8" height="7" viewBox="0 0 10 8"><rect width="10" height="8" fill="#add136"/><path d="M0 0l5 4 5-4" stroke="#fff" fill="none"/></svg>
        <span>bookings@harrowfieldclinic.example</span>
      </li>
    </ul>

    <div class="skyline" role="img" aria-label="Pale grey line drawing of a city skyline"></div>

    <svg class="footer-bands" viewBox="0 0 600 40" aria-hidden="true">
      <polygon points="0,14 425,14 415,40 0,40" fill="var(--clinic-blue)"/>
      <polygon points="432,0 600,0 600,40 417,40" fill="var(--clinic-green)"/>
    </svg>
  </main>
</body>
</html>
```